4' x 20' Residential Contractor Banner

Design Details

Having 4ftW x 20ft W banners printed that will be placed on our construction dumpsters.

Large Logo & company name!

Background Color:
A bold, medium-dark color like charcoal gray or blacks to ensure banner durability while maintaining a clean, professional look in the elements.
Primary Text Layout:

Services:

Basements:
Highlighted in larger, artistic font with a creative touch (e.g., modern script or bold sans-serif with a shadow or glow effect).
Kitchens & Bathrooms:
Use slightly smaller, complementary fonts below "Basements."

Contact Details:

Phone Number: Prominently displayed in bold, easy-to-read font, font displayed can be (612) 947-2186 or 612.947.2186
Website: Clearly visible, prefer it is not placed below the phone number: www.halcyonbuildworks.com.

Social Media: Include the Facebook link with the Facebook icon: facebook.com/halcyonbuildworksmn.
QR Code if possible:

Add a QR code leading to your website or portfolio. Place it near the contact details with a caption like “Scan for More Info!”
Visual Elements:

Subtle design elements like blueprint-style lines, creative icons, or faint textures to add depth without overwhelming.
Branding:

Consistent color accents from branding (e.g., red, black, gray or white).
Size Considerations:
Ensure all text is legible from a distance. Use high-contrast colors (e.g., white or vibrant accents) against the darker background.

Target Market(s)

Residential Signage

Industry/Entity Type

Construction Remodeling

Font styles to use
Sans Serif

Colors
EB3D1F
EC4F4E
F09395
F8D3D4
FCEDEE

Requirements
Must have
• Extra large company logo visibility.
Nice to have
• QR code, social media icons
Should not have
• To much whites

```html
<!DOCTYPE html>
<html lang="en">
<head>
<meta charset="utf-8">
<title>Halcyon Build Works – Dumpster Banner</title>
<link rel="stylesheet" href="https://fonts.googleapis.com/css2?family=Montserrat:wght@600;700;800&display=swap">
<style>
  :root {
    --backdrop: #b3b3b3;
    --charcoal: #231f20;
    --charcoal-soft: #3a3435;
    --red: #d92527;
    --white: #ffffff;
    --outline: rgba(255,255,255,0.75);
  }
  * { box-sizing: border-box; margin: 0; padding: 0; }
  html, body { width: 1200px; height: 446px; overflow: hidden; }
  body {
    background: var(--backdrop);
    font-family: "Montserrat", Arial, sans-serif;
    position: relative;
  }
  .banner {
    position: absolute;
    left: 52px; top: 119px;
    width: 1096px; height: 219px;
    background:
      radial-gradient(ellipse at 30% 40%, rgba(90,80,78,0.35), transparent 60%),
      linear-gradient(90deg, var(--charcoal) 0%, var(--charcoal-soft) 45%, var(--charcoal) 100%);
    overflow: hidden;
  }
  .brand-mark {
    position: absolute;
    left: 12px; top: 20px;
    width: 102px; height: 101px;
    display: flex; flex-direction: column; align-items: center; justify-content: center;
    gap: 10px;
  }
  .brand-square { width: 34px; height: 34px; background: var(--red); }
  .brand-name { color: var(--white); font-weight: 800; font-size: 18px; letter-spacing: 0.5px; }
  .headline {
    position: absolute; left: 137px; top: 22px;
    color: var(--white); font-weight: 800; font-size: 67px; line-height: 1;
    letter-spacing: 0.5px; white-space: nowrap;
    text-shadow: 0 2px 6px rgba(0,0,0,0.5);
  }
  .subline {
    position: absolute; left: 139px; top: 92px;
    color: var(--white); font-weight: 700; font-size: 32.5px; line-height: 1;
    white-space: nowrap;
    text-shadow: 0 2px 4px rgba(0,0,0,0.4);
  }
  .phone-bar {
    position: absolute; left: 0; top: 146px;
    width: 318px; height: 73px;
    background: var(--red);
    border-top-right-radius: 8px;
    display: flex; align-items: center; padding-left: 16px; gap: 8px;
  }
  .phone-icon {
    width: 32px; height: 32px; border-radius: 50%; flex: none;
    background: var(--charcoal); display: flex; align-items: center; justify-content: center;
  }
  .phone-number { color: var(--white); font-weight: 800; font-size: 36px; letter-spacing: 0.3px; white-space: nowrap; }
  .link-pill {
    position: absolute; left: 330px; width: 291px; height: 24px;
    border: 1px solid var(--outline); border-radius: 3px;
    display: flex; align-items: center; gap: 7px; padding-left: 8px;
    color: var(--white); font-weight: 700; white-space: nowrap; overflow: hidden;
  }
  .link-pill.web { top: 147px; font-size: 14px; letter-spacing: 1.3px; }
  .link-pill.social { top: 177px; height: 25px; font-size: 12.6px; letter-spacing: 0.1px; }
  .link-dot { width: 15px; height: 15px; border-radius: 50%; background: var(--red); flex: none; }
  .photo-frame {
    position: absolute; top: 11px; height: 200px;
  }
  .photo-frame.main {
    left: 632px; width: 262px;
    border: 3px solid var(--red); padding: 5px; background: var(--charcoal);
  }
  .photo-frame.stack {
    left: 902px; width: 180px; background: var(--red); padding: 7px;
    display: flex; flex-direction: column; gap: 8px;
  }
  .photo { width: 100%; height: 100%; }
  .photo-frame.stack .photo { flex: 1; }
  .photo.kitchen-bar { background: linear-gradient(180deg, #e6e2dc 0%, #c9c2b8 50%, #5b4535 75%, #d8d0c4 100%); }
  .photo.stairway { background: linear-gradient(160deg, #b9b6b2 0%, #ece9e4 45%, #6e6e70 100%); }
  .photo.family-room { background: linear-gradient(180deg, #9c8a78 0%, #8a6f58 50%, #5a4536 100%); }
</style>
</head>
<body>
  <section class="banner">
    <div class="brand-mark">
      <span class="brand-square"></span>
      <span class="brand-name">HALCYON</span>
    </div>

    <h1 class="headline">BASEMENTS</h1>
    <p class="subline">KITCHENS &amp; BATHROOMS</p>

    <div class="phone-bar">
      <span class="phone-icon">
        <svg width="18" height="18" viewBox="0 0 24 24" fill="none" stroke="#fff" stroke-width="2" stroke-linecap="round" stroke-linejoin="round">
          <path d="M22 16.9v3a2 2 0 0 1-2.2 2 19.8 19.8 0 0 1-8.6-3.1 19.5 19.5 0 0 1-6-6A19.8 19.8 0 0 1 2.1 4.2 2 2 0 0 1 4.1 2h3a2 2 0 0 1 2 1.7c.1.9.4 1.8.7 2.7a2 2 0 0 1-.5 2.1L8 9.8a16 16 0 0 0 6 6l1.3-1.3a2 2 0 0 1 2.1-.4c.9.3 1.8.6 2.7.7a2 2 0 0 1 1.7 2z"/>
        </svg>
      </span>
      <span class="phone-number">612.947.2186</span>
    </div>

    <div class="link-pill web">
      <svg class="link-dot" viewBox="0 0 14 14">
        <circle cx="7" cy="7" r="7" fill="#d92527"/>
        <circle cx="7" cy="7" r="4" fill="none" stroke="#fff" stroke-width="1"/>
        <path d="M3 7h8M7 3c-2 2.5-2 5.5 0 8M7 3c2 2.5 2 5.5 0 8" fill="none" stroke="#fff" stroke-width="0.9"/>
      </svg>
      www.halcyonbuildworks.com
    </div>
    <div class="link-pill social">
      <span class="link-dot"></span>
      friendhub.com/halcyonbuildworksmn
    </div>

    <div class="photo-frame main">
      <div class="photo kitchen-bar" role="img" aria-label="Finished basement wet bar with dark wood cabinets and lit floating shelves"></div>
    </div>
    <div class="photo-frame stack">
      <div class="photo stairway" role="img" aria-label="Remodeled basement stairway opening onto a game area"></div>
      <div class="photo family-room" role="img" aria-label="Basement family room with sofas and a built-in media wall"></div>
    </div>
  </section>
</body>
</html>
```